Vexalturf E-commerce Website Design

I'm looking into having my e-comm website built. We are an investment company that is investing in a private label focused on a rising sport category called Pickleball in EU market.

We will provide top quality material and acessories for players be ready to go to courts. We will have a range of: Rackets, Set of balls, Net, Lines, overgrip, water bottle, player bag.

As it´s a new sports category we would like to see an architecture that alows us to share some storytelling about the category, the brand and lead to purchase of our products.

We will position our self as an inclusive and fun brand that you can reach out to find more info about Pickleball Sport, buy your pickleball stuff and have fun. Its all about action and fun.

Target Market(s)

Europe Market

Industry/Entity Type

Pickleball (Sports)

Coding

Coded - Design and coding required

Number of Pages Required

1 page

Requirements
Must have
• E-commerce look and feel
Nice to have
• A bit of storytelling about the brand and specially the category (Pickleball).

```html
<!DOCTYPE html>
<html lang="en">
<head>
<meta charset="utf-8">
<title>Vexalturf – Pickleball Gear</title>
<link rel="stylesheet" href="https://fonts.googleapis.com/css2?family=Prata&family=Roboto:wght@400;500;700&display=swap">
<style>
:root{
  --orange:#f7941d;
  --navy:#0d3a6b;
  --ink:#1f1f1f;
  --muted:#777;
  --line:#dcdcdc;
  --star:#c5c712;
  --footer:#1c1c1c;
  --white:#fff;
}
*{box-sizing:border-box;margin:0;padding:0}
html,body{width:1200px;height:4095px;overflow:hidden}
body{font-family:'Roboto',sans-serif;color:var(--ink);background:var(--white);position:relative}
.serif{font-family:'Prata',serif;font-weight:400}
.abs{position:absolute}
svg{display:block}

/* header */
.header{position:absolute;top:0;left:0;width:1200px;height:86px}
.logo{left:111px;top:10px;font-size:40px;color:var(--ink)}
.search{left:405px;top:16px;width:358px;height:51px;border:1px solid #e2e2e2;border-radius:26px;box-shadow:0 2px 6px rgba(0,0,0,.08)}
.search span{position:absolute;left:27px;top:17px;font-size:14px;color:#8a8a8a}
.search .go{position:absolute;right:8px;top:8px;width:35px;height:35px;border-radius:50%;background:var(--navy);display:flex;align-items:center;justify-content:center}
.tool{top:18px;width:110px;text-align:center;font-size:13px;font-weight:500}
.tool svg{margin:0 auto 6px}
.tool-sep{top:20px;width:1px;height:44px;background:#e2e2e2}

/* nav */
.nav{top:86px;left:0;width:1200px;height:55px;background:var(--orange)}
.nav .link{position:absolute;top:19px;font-size:14px;font-weight:700;color:var(--white);letter-spacing:.2px}
.nav .account{position:absolute;left:868px;top:0;width:332px;height:55px;background:var(--navy);clip-path:polygon(0 0,100% 0,100% 100%,40px 100%)}
.nav .account span{position:absolute;left:87px;top:19px;font-size:14px;font-weight:700;color:var(--white)}
.nav .account svg{position:absolute;left:204px;top:18px}

/* hero */
.hero{top:141px;left:0;width:1200px;height:585px;background:linear-gradient(120deg,#3b342d 0%,#6a5847 35%,#b59a80 60%,#8b6a4e 80%,#c06a3c 100%)}
.hero-shade{position:absolute;inset:0;background:linear-gradient(90deg,rgba(0,0,0,.45) 0%,rgba(0,0,0,.15) 50%,rgba(0,0,0,0) 100%)}
.hero .pre{left:111px;top:135px;font-size:36px;color:var(--white)}
.hero .big{left:110px;top:178px;font-size:84px;color:var(--white);line-height:1.1}
.hero p{left:111px;top:312px;width:460px;font-size:15px;line-height:22px;color:var(--white);text-align:justify}
.btn{display:flex;align-items:center;justify-content:center;gap:10px;background:var(--orange);color:var(--white);font-weight:700;font-size:13px;border-radius:30px;letter-spacing:.3px}
.hero .btn{left:111px;top:379px;width:168px;height:44px}
.arrow{width:32px;height:30px;background:var(--white);display:flex;align-items:center;justify-content:center}

/* section headings */
.heading{text-align:center;font-size:34px;color:var(--ink)}
.rule{width:50px;height:3px;background:var(--orange);margin:0 auto}

/* categories */
.cats{top:726px;left:0;width:1200px;height:611px}
.cat{position:absolute;top:183px;width:200px;text-align:center}
.cat .pic{width:156px;height:156px;border-radius:50%;margin:0 auto;border:4px solid var(--navy);box-shadow:0 4px 8px rgba(0,0,0,.2)}
.cat.active .pic{border-color:var(--orange)}
.cat .name{margin-top:24px;font-size:22px;font-weight:700}
.cat.active .name{text-decoration:underline;text-underline-offset:4px}

/* about */
.about{top:1337px;left:0;width:1200px;height:575px;background:linear-gradient(90deg,#0c3563 0%,#134579 40%,#5d6f72 62%,#8b8b74 80%,#a4a491 100%)}
.about h2{left:111px;top:64px;font-size:34px;color:var(--white)}
.about .rule{position:absolute;left:111px;top:115px;margin:0}
.about p{left:111px;top:150px;width:494px;font-size:14.4px;line-height:25.7px;color:var(--white);text-align:justify}
.about .btn{left:110px;top:451px;width:236px;height:49px}

/* products */
.products{left:0;width:1200px}
.grid{position:absolute;left:112px;top:164px;width:976px;display:grid;grid-template-columns:repeat(4,226px);column-gap:24px}
.card .thumb{width:226px;height:238px;background:var(--white);box-shadow:0 2px 8px rgba(0,0,0,.2);position:relative;padding:10px}
.card.hot .thumb{border-bottom:3px solid var(--orange)}
.card .photo{width:100%;height:100%}
.card .thumb .cart{position:absolute;right:18px;top:20px}
.card .meta{font-size:13px;color:var(--muted);margin-top:28px}
.card .title{font-size:15px;font-weight:700;margin-top:9px}
.card .stars{color:var(--star);font-size:15px;letter-spacing:2px;margin-top:4px}
.card .price{display:flex;justify-content:space-between;align-items:center;margin-top:6px;border-bottom:1px solid var(--line);font-size:14px;font-weight:700;padding-bottom:2px}
.card .plus{width:22px;height:20px;background:#e6e6e6;color:var(--ink);display:flex;align-items:center;justify-content:center;font-size:17px;font-weight:500}
.card.hot .plus{background:var(--orange);color:var(--white)}

/* testimonials */
.testi{top:2538px;left:0;width:1200px;height:546px;background:linear-gradient(135deg,#f59a2a 0%,#ee8f18 50%,#e58a16 100%)}
.testi h2{position:absolute;top:76px;width:1200px;text-align:center;font-size:34px;color:var(--white)}
.testi .rule{position:absolute;left:575px;top:127px;background:var(--white)}
.testi .intro{position:absolute;left:200px;top:155px;width:800px;text-align:center;font-size:15px;line-height:26px;color:var(--white)}
.quote{position:absolute;top:258px;width:400px;height:198px;background:var(--white);border-radius:26px}
.quote .avatar{position:absolute;left:45px;top:28px;width:66px;height:66px;border-radius:50%;background:linear-gradient(160deg,#9fb4cb,#2c4466)}
.quote .who{position:absolute;left:126px;top:42px;font-size:16px;font-weight:500;color:var(--navy)}
.quote .role{position:absolute;left:126px;top:66px;font-size:12px;color:var(--muted)}
.quote .mark{position:absolute;right:30px;top:32px;font-family:'Prata',serif;font-size:90px;line-height:1;color:#e9e9e9}
.quote p{position:absolute;left:41px;top:114px;width:320px;font-size:13px;line-height:23px;color:#666}

/* footer */
.footer{top:3721px;left:0;width:1200px;height:321px;background:var(--footer)}
.footer .logo{left:113px;top:70px;font-size:38px;color:var(--white)}
.fitem{position:absolute;top:82px;display:flex;gap:18px;color:var(--white)}
.fitem .ic{width:40px;height:40px;border:1px solid #555;border-radius:50%;display:flex;align-items:center;justify-content:center;margin-top:5px}
.fitem b{display:block;font-size:12px;margin-bottom:6px}
.fitem span{font-size:13px;line-height:20px}
.fitem .strong{font-size:16px;font-weight:700}
.footer .divider{position:absolute;left:113px;top:160px;width:975px;height:1px;background:#3a3a3a}
.social{position:absolute;top:184px;width:35px;height:35px;border-radius:50%;border:1px solid var(--orange)}
.fnav{position:absolute;top:259px;width:1200px;display:flex;justify-content:center;gap:30px;color:var(--white);font-size:15px;font-weight:700}
.copy{top:4042px;left:0;width:1200px;height:53px;background:var(--orange);color:var(--white);font-size:13px;text-align:center;line-height:53px}
</style>
</head>
<body>

<header class="header">
  <div class="abs logo serif">Vexalturf</div>
  <div class="abs search"><span>Search Products</span>
    <div class="go"><svg width="14" height="14" viewBox="0 0 14 14"><circle cx="6" cy="6" r="4" fill="none" stroke="#fff" stroke-width="2"/><path d="M9 9l3.5 3.5" stroke="#fff" stroke-width="2" stroke-linecap="round"/></svg></div>
  </div>
  <div class="abs tool" style="left:786px"><svg width="15" height="13" viewBox="0 0 24 21"><path d="M12 21L2 11A6 6 0 0112 3a6 6 0 0110 8z" fill="#f7941d"/></svg>Wishlist</div>
  <div class="abs tool-sep" style="left:886px"></div>
  <div class="abs tool" style="left:891px"><svg width="12" height="13" viewBox="0 0 12 13"><circle cx="6" cy="3.5" r="3.2" fill="#f7941d"/><path d="M0 13c0-4 2.7-6 6-6s6 2 6 6z" fill="#f7941d"/></svg>My Accounts</div>
  <div class="abs tool-sep" style="left:1000px"></div>
  <div class="abs tool" style="left:1000px"><svg width="14" height="13" viewBox="0 0 14 13"><path d="M0 1h2.5l2 7.5h7.5L14 3H4" fill="none" stroke="#f7941d" stroke-width="1.8"/><circle cx="5.5" cy="11.5" r="1.3" fill="#f7941d"/><circle cx="11" cy="11.5" r="1.3" fill="#f7941d"/></svg>( 0 Items )</div>
</header>

<nav class="abs nav">
  <span class="link" style="left:113px">HOME</span>
  <span class="link" style="left:203px">ABOUT US</span>
  <span class="link" style="left:322px">SHOP</span>
  <span class="link" style="left:410px">OUR PRODUCTS</span>
  <span class="link" style="left:573px">TESTIMONIALS</span>
  <span class="link" style="left:728px">CONTACT US</span>
  <div class="account"><span>SIGIN / LOGIN</span>
    <svg width="12" height="14" viewBox="0 0 12 13"><circle cx="6" cy="3.5" r="3.2" fill="#fff"/><path d="M0 13c0-4 2.7-6 6-6s6 2 6 6z" fill="#fff"/></svg>
  </div>
</nav>

<section class="abs hero" role="img" aria-label="Close-up of a pickleball paddle striking a yellow ball on a clay court">
  <div class="hero-shade"></div>
  <div class="abs pre serif">Welcome to</div>
  <div class="abs big serif">Vexalturf</div>
  <p class="abs">Lorem ipsum dolor sited ameted consectetur adipiscing elited eiusmod tempor incididunt labore dolore magna aliquad.</p>
  <div class="abs btn">SHOP NOW
    <svg width="14" height="13" viewBox="0 0 14 13"><path d="M0 1h2.5l2 7.5h7.5L14 3H4" fill="none" stroke="#fff" stroke-width="1.8"/><circle cx="5.5" cy="11.5" r="1.3" fill="#fff"/><circle cx="11" cy="11.5" r="1.3" fill="#fff"/></svg>
  </div>
  <div class="abs arrow" style="left:38px;top:268px"><svg width="8" height="14" viewBox="0 0 8 14"><path d="M7 1L1 7l6 6" fill="none" stroke="#333" stroke-width="1.5"/></svg></div>
  <div class="abs arrow" style="left:1130px;top:268px"><svg width="8" height="14" viewBox="0 0 8 14"><path d="M1 1l6 6-6 6" fill="none" stroke="#333" stroke-width="1.5"/></svg></div>
</section>

<section class="abs cats">
  <h2 class="heading serif" style="position:absolute;top:80px;width:1200px">Shop By Categories</h2>
  <div class="rule" style="position:absolute;left:575px;top:135px"></div>
  <div class="cat" style="left:108px"><div class="pic" role="img" aria-label="Player holding a racket" style="background:linear-gradient(160deg,#c9a27d,#7a4e36)"></div><div class="name">Rackets</div></div>
  <div class="cat" style="left:308px"><div class="pic" role="img" aria-label="Yellow balls on a court" style="background:linear-gradient(160deg,#d8b388,#b4553a)"></div><div class="name">Set of balls</div></div>
  <div class="cat active" style="left:509px"><div class="pic" role="img" aria-label="Player bag on a bench" style="background:linear-gradient(160deg,#6a8a3a,#a0522d)"></div><div class="name" style="margin-top:34px">Player bag</div></div>
  <div class="cat" style="left:709px"><div class="pic" role="img" aria-label="Water bottle beside a net" style="background:linear-gradient(160deg,#8fb6d8,#c2713f)"></div><div class="name" style="margin-top:30px">Water bottle</div></div>
  <div class="cat" style="left:909px"><div class="pic" role="img" aria-label="Hands wrapping an overgrip" style="background:linear-gradient(160deg,#e6ded8,#b8826a)"></div><div class="name" style="margin-top:34px">Overgrip</div></div>
  <div class="abs btn" style="left:482px;top:467px;width:236px;height:50px">VIEW ALL CATEGORIES
    <svg width="14" height="14" viewBox="0 0 14 14"><circle cx="7" cy="7" r="7" fill="#fff"/><path d="M5.5 4l3 3-3 3" fill="none" stroke="#f7941d" stroke-width="1.8"/></svg>
  </div>
</section>

<section class="abs about" role="img" aria-label="Player on a court with a paddle resting against the net">
  <h2 class="abs serif">About Vexalturf</h2>
  <div class="rule"></div>
  <p class="abs">Lorem ipsum dolor sit amet, consectetur adipiscing elit, sed do eiusmod tempor incididunt ut labore et dolore magna aliqua. Ut enim ad minim veniam, quis nostrud exercitation ullamco laboris nisi ut aliquip ex ea commodo consequat. Duis aute irure dolor in reprehenderit in voluptate velit esse cillum dolore eu fugiat nulla pariatur. Excepteur sint occaecat cupidatat non proident, sunt in culpa qui officia deserunt mollit anim id est laborumLorem ipsum dolor sit amet, consectetur adipiscing elit, sed do eiusmod tempor incididunt ut labore et dolore magna aliqua. Ut enim ad minim veniam, quis nostrud exercitation ullamco laboris nisi ut aliquip ex ea commodo consequat. Duis aute irure dolor in reprehenderit in voluptate velit esse cillum dolore eu fugiat nulla pariatur.</p>
  <div class="abs btn">SHOP PRODUCTS
    <svg width="14" height="13" viewBox="0 0 14 13"><path d="M0 1h2.5l2 7.5h7.5L14 3H4" fill="none" stroke="#fff" stroke-width="1.8"/><circle cx="5.5" cy="11.5" r="1.3" fill="#fff"/><circle cx="11" cy="11.5" r="1.3" fill="#fff"/></svg>
  </div>
</section>

<section class="abs products" style="top:1912px;height:626px">
  <h2 class="heading serif" style="position:absolute;top:78px;width:1200px">Featured Products</h2>
  <div class="rule" style="position:absolute;left:575px;top:133px"></div>
  <div class="grid">
    <div class="card"><div class="thumb"><div class="photo" role="img" aria-label="Product photo: black racket with a yellow ball" style="background:radial-gradient(ellipse at center,#c9c9c4 0%,#f2f2ef 55%,#fff 80%)"></div></div>
      <div class="meta">Lorem ipsum dolor sit ameted</div><div class="title">Product Title</div><div class="stars">★★★★★</div><div class="price">$50.00<span class="plus">+</span></div></div>
    <div class="card"><div class="thumb"><div class="photo" role="img" aria-label="Product photo: black water bottle" style="background:radial-gradient(ellipse at center,#bdbdbd 0%,#eeeeee 50%,#fff 80%)"></div></div>
      <div class="meta">Lorem ipsum dolor sit ameted</div><div class="title">Product Title</div><div class="stars">★★★★★</div><div class="price">$50.00<span class="plus">+</span></div></div>
    <div class="card hot"><div class="thumb"><div class="photo" role="img" aria-label="Product photo: yellow ball" style="background:radial-gradient(ellipse at center,#e4eb9a 0%,#f6f8dd 50%,#fff 80%)"></div><svg class="cart" width="14" height="13" viewBox="0 0 14 13"><path d="M0 1h2.5l2 7.5h7.5L14 3H4" fill="none" stroke="#f7941d" stroke-width="1.8"/><circle cx="5.5" cy="11.5" r="1.3" fill="#f7941d"/><circle cx="11" cy="11.5" r="1.3" fill="#f7941d"/></svg></div>
      <div class="meta">Lorem ipsum dolor sit ameted</div><div class="title">Product Title</div><div class="stars">★★★★★</div><div class="price">$50.00<span class="plus">+</span></div></div>
    <div class="card"><div class="thumb"><div class="photo" role="img" aria-label="Product photo: orange and navy player bag" style="background:radial-gradient(ellipse at center,#f3cf86 0%,#f8ecd4 50%,#fff 80%)"></div></div>
      <div class="meta">Lorem ipsum dolor sit ameted</div><div class="title">Product Title</div><div class="stars">★★★★★</div><div class="price">$50.00<span class="plus">+</span></div></div>
  </div>
</section>

<section class="abs testi">
  <h2 class="serif">Our Testimonials</h2>
  <div class="rule"></div>
  <p class="intro">Lorem ipsum dolor sit amet consectetur adipiscing elit sed do eiusmod tempor incididunt ut labore et dolore magna aliqua. Ut enim ad minim veniam, quis nostrud exercitation ullamco laboris nisi u consequat.</p>
  <div class="quote" style="left:184px">
    <div class="avatar" role="img" aria-label="Customer portrait"></div>
    <div class="who">Liam Corvel</div><div class="role">Lorem ipsum dolor sit</div><div class="mark">“</div>
    <p>Lorem ipsum dolor ameted consectetur adipiscing elit sed do eiusmod tempor incididunt ut labore ete dolore magna incididunt ut labore aliquad.</p>
  </div>
  <div class="quote" style="left:617px">
    <div class="avatar" role="img" aria-label="Customer portrait"></div>
    <div class="who">Liam Corvel</div><div class="role">Lorem ipsum dolor sit</div><div class="mark">“</div>
    <p>Lorem ipsum dolor ameted consectetur adipiscing elit sed do eiusmod tempor incididunt ut labore ete dolore magna incididunt ut labore aliquad.</p>
  </div>
  <div class="abs arrow" style="left:35px;top:341px"><svg width="8" height="14" viewBox="0 0 8 14"><path d="M7 1L1 7l6 6" fill="none" stroke="#333" stroke-width="1.5"/></svg></div>
  <div class="abs arrow" style="left:1125px;top:341px"><svg width="8" height="14" viewBox="0 0 8 14"><path d="M1 1l6 6-6 6" fill="none" stroke="#333" stroke-width="1.5"/></svg></div>
</section>

<section class="abs products" style="top:3084px;height:637px">
  <h2 class="heading serif" style="position:absolute;top:80px;width:1200px">Best Seller</h2>
  <div class="rule" style="position:absolute;left:575px;top:127px"></div>
  <div class="grid" style="left:114px;top:171px">
    <div class="card"><div class="thumb"><div class="photo" role="img" aria-label="Product photo: rolled black overgrips" style="background:radial-gradient(ellipse at center,#b8b8b8 0%,#ececec 50%,#fff 80%)"></div></div>
      <div class="meta">Lorem ipsum dolor sit ameted</div><div class="title">Product Title</div><div class="stars">★★★★★</div><div class="price">$50.00<span class="plus">+</span></div></div>
    <div class="card"><div class="thumb"><div class="photo" role="img" aria-label="Product photo: yellow ball" style="background:radial-gradient(ellipse at center,#e4eb9a 0%,#f6f8dd 50%,#fff 80%)"></div></div>
      <div class="meta">Lorem ipsum dolor sit ameted</div><div class="title">Product Title</div><div class="stars">★★★★★</div><div class="price">$50.00<span class="plus">+</span></div></div>
    <div class="card hot"><div class="thumb"><div class="photo" role="img" aria-label="Product photo: red and white racket" style="background:radial-gradient(ellipse at center,#ecc4c4 0%,#f7ecec 50%,#fff 80%)"></div><svg class="cart" width="14" height="13" viewBox="0 0 14 13"><path d="M0 1h2.5l2 7.5h7.5L14 3H4" fill="none" stroke="#f7941d" stroke-width="1.8"/><circle cx="5.5" cy="11.5" r="1.3" fill="#f7941d"/><circle cx="11" cy="11.5" r="1.3" fill="#f7941d"/></svg></div>
      <div class="meta">Lorem ipsum dolor sit ameted</div><div class="title">Product Title</div><div class="stars">★★★★★</div><div class="price">$50.00<span class="plus">+</span></div></div>
    <div class="card"><div class="thumb"><div class="photo" role="img" aria-label="Product photo: red and black paddles with a ball" style="background:radial-gradient(ellipse at center,#e3a9a2 0%,#f5e3e0 50%,#fff 80%)"></div></div>
      <div class="meta">Lorem ipsum dolor sit ameted</div><div class="title">Product Title</div><div class="stars">★★★★★</div><div class="price">$50.00<span class="plus">+</span></div></div>
  </div>
</section>

<footer class="abs footer">
  <div class="abs logo serif">Vexalturf</div>
  <div class="fitem" style="left:327px">
    <div class="ic"><svg width="12" height="16" viewBox="0 0 12 16"><path d="M6 16S0 9 0 6a6 6 0 0112 0c0 3-6 10-6 10z" fill="#f7941d"/><circle cx="6" cy="6" r="2.2" fill="#1c1c1c"/></svg></div>
    <div><b>ADDRESS :</b><span>142, Lorem ipsum dolor<br>sitED sed do eiusmod</span></div>
  </div>
  <div class="fitem" style="left:599px">
    <div class="ic"><svg width="15" height="15" viewBox="0 0 16 16"><path d="M3 1l3 3-2 2c1 2 3 4 5 5l2-2 3 3-2 3C6 15 1 10 0 4z" fill="#f7941d"/></svg></div>
    <div><b>PHONE NO :</b><span class="strong">+ 1 555 014 2270</span></div>
  </div>
  <div class="fitem" style="left:876px">
    <div class="ic"><svg width="15" height="11" viewBox="0 0 15 11"><rect width="15" height="11" rx="1.5" fill="#f7941d"/><path d="M1 1.5l6.5 5 6.5-5" fill="none" stroke="#1c1c1c" stroke-width="1.4"/></svg></div>
    <div><b>EMAIL ADDRESS :</b><span style="font-size:15px">info@vexalturf.com</span></div>
  </div>
  <div class="divider"></div>
  <div class="social" style="left:539px"></div>
  <div class="social" style="left:582px"></div>
  <div class="social" style="left:625px"></div>
  <div class="fnav"><span>HOME</span><span>/</span><span>ABOUT US</span><span>/</span><span>SHOP</span><span>/</span><span>OUR PRODUCTS</span><span>/</span><span>TESTIMONIALS</span><span>/</span><span>CONTACT US</span></div>
</footer>
<div class="abs copy">Copyright © 2023 Vexalturf. All Rights Reserved</div>

</body>
</html>
```